Zielgruppe
Wir sind ein Landwirtschaftsbetrieb für Obstbau und unsere Kunden sind hauptsächlich Privatpersonen und Familien aus der Region sowie Kleinbetriebe wie z. B. regionale Shops.
Aufgabenstellung
Wir benötigen Flaschenetiketten für Fruchtsäfte (3 verschiedene Sorten: Marillennektar, Pfirsichnektar, Kirschennektar) für 0,75 und 0,25 Liter Flaschen und für Schnaps und Liköre (Marillen, Kirschen, Pfirsich, Zwetschke, Kriecherl).
Wir würden eine Vorderseite, die das Design und die Pflichtangaben enthält, bevorzugen.
Die Schrift der Pflichtangaben muss wie folgt ausgeführt werden: Etiketten bis 80 cm2 Kleinbuchstaben mind. 0,9 mm, ab 80 cm2 Kleinbuchstaben mind. 1,2 mm, Großbuchstaben immer mind. 2 mm, das Feld benötigt in etwa 3,5 x 7 cm Platz. Für das Design gibt es noch keine fixe Größe.
Bitte keine Fotos von 'echtem' Obst verwenden.

```html
<!DOCTYPE html>
<html lang="de">
<head>
<meta charset="utf-8">
<title>Kirschen Nektar – Etikett</title>
<link href="https://fonts.googleapis.com/css2?family=Oswald:wght@300;500&family=Roboto+Condensed:wght@400;700&display=swap" rel="stylesheet">
<style>
  :root {
    --cherry: #c4262e;
    --cherry-dark: #a51d24;
    --ember: #e8652a;
    --blush: #f7d9d9;
    --mist: #e3e8e8;
    --bracket: #f06aa0;
    --ink: #7a1a1f;
    --paper: #ffffff;
    --backdrop: #f4f4f4;
  }
  * { margin: 0; padding: 0; box-sizing: border-box; }
  html, body { width: 713px; height: 1200px; overflow: hidden; background: var(--backdrop); }
  .canvas { position: relative; width: 713px; height: 1200px; }
  .label {
    position: absolute; left: 36px; top: 207px; width: 640px; height: 785px;
    background: var(--paper); box-shadow: 0 10px 30px rgba(0,0,0,.12);
    font-family: "Roboto Condensed", sans-serif;
  }
  .label-art { position: absolute; inset: 0; }
  .brand {
    position: absolute; left: 0; right: 0; top: 46px;
    display: flex; justify-content: center; align-items: center; gap: 6px;
    font-family: "Roboto Condensed", sans-serif; font-weight: 700; font-size: 13px;
    letter-spacing: .06em; color: var(--cherry); text-transform: uppercase;
  }
  .brand-dot { width: 10px; height: 10px; border-radius: 50%; background: var(--cherry); }
  .title {
    position: absolute; left: 0; right: 0; top: 208px; text-align: center;
    font-family: "Oswald", sans-serif; font-weight: 300; color: var(--cherry);
    font-size: 58px; line-height: 62px;
  }
  .volume {
    position: absolute; left: 0; right: 0; top: 580px; text-align: center;
    font-family: "Oswald", sans-serif; font-weight: 300; font-size: 34px; color: var(--cherry-dark);
  }
  .producer {
    position: absolute; left: 0; right: 0; top: 638px; text-align: center;
    font-weight: 700; font-size: 15px; color: var(--ink);
  }
  .facts {
    position: absolute; left: 90px; right: 90px; top: 661px; text-align: center;
    font-size: 8px; line-height: 13px; color: var(--ink);
  }
</style>
</head>
<body>
<div class="canvas">
  <div class="label">
    <svg class="label-art" width="640" height="785" viewBox="0 0 640 785">
      <defs>
        <linearGradient id="archStroke" x1="0" y1="0" x2="0" y2="1">
          <stop offset="0" stop-color="#e8652a"/>
          <stop offset=".35" stop-color="#c4262e"/>
          <stop offset="1" stop-color="#a51d24"/>
        </linearGradient>
        <linearGradient id="footBar" x1="0" y1="0" x2="1" y2="0">
          <stop offset="0" stop-color="#b81f27"/>
          <stop offset=".5" stop-color="#e8652a"/>
          <stop offset="1" stop-color="#b81f27"/>
        </linearGradient>
        <linearGradient id="foliage" x1="0" y1="0" x2="1" y2="1">
          <stop offset="0" stop-color="#f3f5f5"/>
          <stop offset=".5" stop-color="#e6ebeb"/>
          <stop offset="1" stop-color="#f8e6e6"/>
        </linearGradient>
        <linearGradient id="cherryFill" x1="0" y1="0" x2="0" y2="1">
          <stop offset="0" stop-color="#5fa84a"/>
          <stop offset=".4" stop-color="#d8323a"/>
          <stop offset="1" stop-color="#b5222a"/>
        </linearGradient>
      </defs>

      <g class="corner-brackets" fill="none" stroke="var(--bracket)" stroke-width="4">
        <path d="M234 51 H51 V251"/>
        <path d="M406 51 H589 V251"/>
      </g>

      <g role="img" aria-label="Zarte Blätter- und Kirschendekoration im Hintergrund">
        <path d="M82 730 V390 A260 260 0 0 1 600 390 V730 Z" fill="url(#foliage)"/>
      </g>

      <circle class="title-disc" cx="343" cy="251" r="92" fill="var(--blush)"/>

      <path class="arch" d="M74 755 V390 A268 268 0 0 1 608 390 V755"
            fill="none" stroke="url(#archStroke)" stroke-width="16"/>
      <rect class="arch-foot" x="66" y="730" width="550" height="25" fill="url(#footBar)"/>

      <g role="img" aria-label="Illustration zweier Kirschen mit Blatt">
        <rect x="250" y="352" width="186" height="206" rx="60" fill="url(#cherryFill)"/>
      </g>
    </svg>

    <div class="brand"><span class="brand-dot"></span>Obstbau-Lindner</div>
    <h1 class="title">KIRSCHEN<br>• NEKTAR •</h1>
    <div class="volume">.75L</div>
    <p class="producer">Josef Lindner, Kirchweg 14, A-2000 Auental</p>
    <p class="facts">
      Zutaten: Wasser, Fruchtfleisch, Zucker, Säuerungsmittel: Zitronensäure, Antioxidationsmittel: Ascorbinsäure<br>
      Kühl und dunkel lagern; vor dem Öffnen schütteln und innerhalb einiger Tage konsumieren.<br>
      Mindestens haltbar siehe Verschluss.<br>
      Marillen aus eigener Produktion
    </p>
  </div>
</div>
</body>
</html>
```